Four In The Door Direct Postcard Marketing Campaign.

I would like a series of four postcards for a direct mail campaign. They will be sent out once a week. The campaign is aimed at human resources professionals. We are a 25 year old staffing company breaking into a new market. I would like a funny or creative campaign built around the theme "All Things Employees" Our company strengths lie in our responsive customer service, our integrity, our expertise and our professionalism. Our website is www.alliedwithmavens.com if you would like more information about our company. Our company colors are red, white and black. I like statistics, quotes, etc. I would like to get the campaign out in early December so Iam working on a tight schedule.

Target Market(s)

Human Resources Managers
Plant Managers
Business Owners

Industry/Entity Type

Marketing

Requirements
Must have
• Tag Line All Things Employees or Allied with Mavens

```html
<!DOCTYPE html>
<html lang="en">
<head>
<meta charset="utf-8">
<title>Harborline Staffing – Allied with Mavens</title>
<link rel="stylesheet" href="https://fonts.googleapis.com/css2?family=Source+Sans+3:wght@400;700&display=swap">
<style>
  :root {
    --card-bg: #dfe6f2;
    --brand-red: #c8202f;
    --bar-blue: #2d62a0;
    --bar-green: #8cc63f;
    --ink-grey: #555a60;
    --accent-pink: #e4cfd0;
    --photo-mid: #c9c6c2;
  }
  html, body {
    margin: 0;
    padding: 0;
    width: 1200px;
    height: 798px;
    overflow: hidden;
    background: var(--card-bg);
  }
  .postcard {
    position: relative;
    width: 1200px;
    height: 798px;
    overflow: hidden;
    background: var(--card-bg);
    font-family: "Source Sans 3", "Myriad Pro", sans-serif;
  }
  .layer {
    position: absolute;
    inset: 0;
    width: 1200px;
    height: 798px;
  }
  .team-photo {
    position: absolute;
    left: 508px;
    top: 237px;
    width: 692px;
    height: 561px;
    background:
      radial-gradient(ellipse at 50% 55%, var(--photo-mid) 0%, rgba(201,198,194,0.6) 45%, rgba(223,230,242,0) 75%);
  }
  .brand {
    position: absolute;
    left: 57px;
    top: 40px;
    display: flex;
    align-items: center;
    gap: 12px;
  }
  .brand-dot {
    width: 50px;
    height: 50px;
    border-radius: 50%;
    background: var(--brand-red);
  }
  .brand-name {
    margin: 0;
    color: var(--brand-red);
    font-weight: 700;
    font-size: 37px;
    line-height: 34px;
  }
  .brand-tagline {
    position: absolute;
    left: 57px;
    width: 292px;
    top: 116px;
    margin: 0;
    text-align: right;
    color: var(--ink-grey);
    font-size: 14px;
  }
  .pitch {
    position: absolute;
    right: 32px;
    top: 36px;
    margin: 0;
    text-align: right;
    color: var(--brand-red);
    font-size: 26px;
    line-height: 36px;
    font-weight: 400;
  }
  .headline {
    position: absolute;
    right: 32px;
    top: 146px;
    margin: 0;
    color: var(--brand-red);
    font-size: 46px;
    line-height: 56px;
    font-weight: 700;
    letter-spacing: -0.5px;
  }
</style>
</head>
<body>
<main class="postcard">
  <svg class="layer backdrop" viewBox="0 0 1200 798" aria-hidden="true">
    <circle cx="721" cy="140" r="123" fill="var(--accent-pink)" opacity="0.8"/>
  </svg>

  <div class="team-photo" role="img" aria-label="Photo of a cheerful group of office staff raising their hands"></div>

  <svg class="layer staffing-chart" viewBox="0 0 1200 798" aria-hidden="true">
    <g class="bar-green" fill="var(--bar-green)">
      <rect x="0" y="198" width="30" height="600"/>
      <rect x="36" y="258" width="30" height="540"/>
      <rect x="72" y="313" width="30" height="485"/>
      <rect x="108" y="363" width="30" height="435"/>
      <rect x="144" y="408" width="30" height="390"/>
      <rect x="180" y="448" width="30" height="350"/>
      <rect x="216" y="483" width="30" height="315"/>
      <rect x="252" y="515" width="30" height="283"/>
      <rect x="288" y="543" width="30" height="255"/>
      <rect x="324" y="568" width="30" height="230"/>
      <rect x="360" y="591" width="30" height="207"/>
      <rect x="396" y="612" width="30" height="186"/>
      <rect x="432" y="631" width="30" height="167"/>
      <rect x="468" y="648" width="30" height="150"/>
      <rect x="504" y="663" width="30" height="135"/>
      <rect x="540" y="677" width="30" height="121"/>
      <rect x="576" y="689" width="30" height="109"/>
      <rect x="612" y="700" width="30" height="98"/>
      <rect x="648" y="710" width="30" height="88"/>
      <rect x="684" y="719" width="30" height="79"/>
    </g>
    <g class="bar-red" fill="var(--brand-red)">
      <rect x="0" y="258" width="30" height="540"/>
      <rect x="36" y="312" width="30" height="486"/>
      <rect x="72" y="362" width="30" height="436"/>
      <rect x="108" y="406" width="30" height="392"/>
      <rect x="144" y="446" width="30" height="352"/>
      <rect x="180" y="482" width="30" height="316"/>
      <rect x="216" y="514" width="30" height="284"/>
      <rect x="252" y="543" width="30" height="255"/>
      <rect x="288" y="568" width="30" height="230"/>
      <rect x="324" y="590" width="30" height="208"/>
      <rect x="360" y="611" width="30" height="187"/>
      <rect x="396" y="630" width="30" height="168"/>
      <rect x="432" y="647" width="30" height="151"/>
      <rect x="468" y="662" width="30" height="136"/>
      <rect x="504" y="676" width="30" height="122"/>
      <rect x="540" y="689" width="30" height="109"/>
      <rect x="576" y="700" width="30" height="98"/>
      <rect x="612" y="709" width="30" height="89"/>
      <rect x="648" y="719" width="30" height="79"/>
      <rect x="684" y="727" width="30" height="71"/>
    </g>
    <g class="bar-blue" fill="var(--bar-blue)">
      <rect x="0" y="408" width="30" height="390"/>
      <rect x="36" y="447" width="30" height="351"/>
      <rect x="72" y="483" width="30" height="315"/>
      <rect x="108" y="515" width="30" height="283"/>
      <rect x="144" y="544" width="30" height="254"/>
      <rect x="180" y="570" width="30" height="228"/>
      <rect x="216" y="593" width="30" height="205"/>
      <rect x="252" y="614" width="30" height="184"/>
      <rect x="288" y="632" width="30" height="166"/>
      <rect x="324" y="648" width="30" height="150"/>
      <rect x="360" y="663" width="30" height="135"/>
      <rect x="396" y="677" width="30" height="121"/>
      <rect x="432" y="689" width="30" height="109"/>
      <rect x="468" y="700" width="30" height="98"/>
      <rect x="504" y="710" width="30" height="88"/>
      <rect x="540" y="719" width="30" height="79"/>
      <rect x="576" y="727" width="30" height="71"/>
      <rect x="612" y="734" width="30" height="64"/>
      <rect x="648" y="741" width="30" height="57"/>
      <rect x="684" y="747" width="30" height="51"/>
    </g>
  </svg>

  <header class="brand">
    <span class="brand-dot" aria-hidden="true"></span>
    <p class="brand-name">Harborline<br>Staffing</p>
  </header>
  <p class="brand-tagline">Allied with Mavens.</p>

  <p class="pitch">Harborline offers guidance, in-depth knowledge,<br>and expertise to successfully counsel our clients in<br>all of their human resources needs.</p>
  <h1 class="headline">Allied with Mavens.</h1>
</main>
</body>
</html>
```